Business Card Design for Event Planning Company

Create a business card for event planning company using our new logo. After I pick the design, I will need files made for 6 employees. Our company provides event design & logistics services as well as venue management. The font should be sans serif and complementary to the logo. I will need to know the name of the font selected for the final design. The phone numbers listed should be separated by "." not "-"

Address for the card
PO Box 318, Washington, DC 20019

Card One
Lorna Pettibone
lpettibone@galavoyant.com
202.481.7730

Card Two
Miriam Okonkwo
mokonkwo@galavoyant.com
202.556.2047

Card Three
Tessa Varnholt
tvarnholt@galavoyant.com
978.620.4471

Card Four
Robin Fess
rfess@galavoyant.com
202.718.3362

Card Five
Ada-Rose Pelletan-Uzor
adarose@galavoyant.com
202.839.1205

Card Six
Beatrix Holloway
Beatrix@galavoyant.com
202.492.6618

Target Market(s)

Corporate/Non-Profit

Industry/Entity Type

Event Planning

Contact Information for Business Card

Address for the card

Card One
Lorna Pettibone
lpettibone@galavoyant.com
202.481.7730

Card Two
Miriam Okonkwo
202.556.2047

Card Three
Tessa Varnholt
978.620.4471

Card Four
Robin Fess
rfess@galavoyant.com
202.718.3362

Card Five
Ada-Rose Pelletan-Uzor
202.839.1205

Card Six
Beatrix Holloway
202.492.6618

Font styles to use
Sans Serif

Colors

Designer to choose colors to be used in the design.

Requirements
Must have
• Two-sided with logo
Should not have
• Extra colors or be too busy

```html
<!DOCTYPE html>
<html lang="en">
<head>
<meta charset="utf-8">
<title>Galavoyant Business Card</title>
<link rel="stylesheet" href="https://fonts.googleapis.com/css2?family=Questrial&family=Open+Sans:wght@400&display=swap">
<style>
  :root {
    --page: #ffffff;
    --card: #333637;
    --panel-outer: #343637;
    --panel-inner: #39393b;
    --stripe-deep: #138c9e;
    --stripe-mid: #15b5cc;
    --stripe-light: #52c8e8;
    --ribbon: #135e6b;
    --ribbon-fold: #1d3b3f;
    --icon-tab: #333637;
    --accent: #5aa3a3;
    --ink: #000000;
    --text-light: #ffffff;
  }
  html, body {
    margin: 0;
    padding: 0;
    width: 1200px;
    height: 1200px;
    overflow: hidden;
    background: var(--page);
  }
  .canvas { display: block; width: 1200px; height: 1200px; }
  .card-bg { fill: var(--card); }
  .stripe-deep { fill: var(--stripe-deep); }
  .stripe-mid { fill: var(--stripe-mid); }
  .stripe-light { fill: var(--stripe-light); }
  .ribbon { fill: var(--ribbon); }
  .ribbon-fold { fill: var(--ribbon-fold); }
  .icon-tab { fill: var(--icon-tab); }
  .icon { fill: var(--text-light); }
  .contact-text {
    font-family: "Open Sans", sans-serif;
    fill: var(--text-light);
  }
  .holder-name {
    font-family: "Questrial", sans-serif;
    font-size: 48px;
    letter-spacing: 14px;
    fill: var(--accent);
  }
  .name-rule { fill: var(--ink); }
  .brand-name {
    font-family: "Questrial", sans-serif;
    fill: var(--accent);
  }
  .panel-outer { fill: var(--panel-outer); stroke: url(#edgeGlow); stroke-width: 1.5; }
  .panel-inner { fill: var(--panel-inner); stroke: url(#edgeGlow); stroke-width: 1.5; }
</style>
</head>
<body>
<svg class="canvas" viewBox="0 0 1500 1500" xmlns="http://www.w3.org/2000/svg">
  <defs>
    <clipPath id="frontClip"><rect x="215" y="135" width="1030" height="588" rx="40"/></clipPath>
    <clipPath id="backClip"><rect x="220" y="775" width="1030" height="590" rx="40"/></clipPath>
    <linearGradient id="edgeGlow" x1="0" y1="0" x2="1" y2="0">
      <stop offset="0" stop-color="#2c3a8a"/>
      <stop offset="1" stop-color="#8cc63f"/>
    </linearGradient>
    <filter id="panelShadow" x="-5%" y="-5%" width="110%" height="115%">
      <feDropShadow dx="0" dy="4" stdDeviation="5" flood-color="#000" flood-opacity="0.45"/>
    </filter>
  </defs>

  <!-- Front of card -->
  <g class="card-front">
    <rect class="card-bg" x="215" y="135" width="1030" height="588" rx="40"/>
    <g clip-path="url(#frontClip)">
      <polygon class="stripe-deep" points="262,135 370,135 493,723 385,723"/>
      <polygon class="stripe-mid" points="370,135 477,135 600,723 493,723"/>
      <polygon class="stripe-light" points="477,135 585,135 709,723 600,723"/>

      <!-- Address ribbon -->
      <polygon class="ribbon-fold" points="606,245 658,270 606,270"/>
      <polygon class="ribbon-fold" points="255,350 310,350 310,374"/>
      <rect class="ribbon" x="255" y="270" width="403" height="80"/>
      <polygon class="icon-tab" points="296,285 344,285 356,334 308,334"/>
      <path class="icon" d="M326,293 a10,10 0 0 1 10,10 c0,7 -10,18 -10,18 c0,0 -10,-11 -10,-18 a10,10 0 0 1 10,-10 z M326,299 a4,4 0 1 0 0.01,0 z" fill-rule="evenodd"/>
      <text class="contact-text" font-size="19" x="379" y="309">PO Box 318,</text>
      <text class="contact-text" font-size="19" x="405" y="335">Washington, DC 20019</text>

      <!-- Email ribbon -->
      <polygon class="ribbon-fold" points="640,403 692,427 640,427"/>
      <polygon class="ribbon-fold" points="290,505 345,505 345,529"/>
      <rect class="ribbon" x="290" y="427" width="402" height="78"/>
      <polygon class="icon-tab" points="318,440 366,440 378,489 330,489"/>
      <g class="icon">
        <rect x="333" y="452" width="29" height="21" fill="#fff"/>
        <polyline points="334,453 347.5,465 361,453" fill="none" stroke="#333637" stroke-width="2"/>
        <polyline points="334,472 344,462 M351,462 361,472" fill="none" stroke="#333637" stroke-width="1.5"/>
      </g>
      <text class="contact-text" font-size="22" x="391" y="472">Name@galavoyant.com</text>

      <!-- Phone ribbon -->
      <polygon class="ribbon-fold" points="683,559 735,583 683,583"/>
      <polygon class="ribbon-fold" points="333,661 388,661 388,685"/>
      <rect class="ribbon" x="333" y="583" width="402" height="78"/>
      <polygon class="icon-tab" points="362,597 410,597 422,647 374,647"/>
      <path class="icon" d="M381,609 l7,-3 l6,10 l-5,4 c2,5 5,8 10,10 l4,-5 l10,6 l-3,7 c-16,1 -30,-13 -29,-29 z"/>
      <text class="contact-text" font-size="36" x="441" y="635">000.000.0000</text>
    </g>

    <text class="holder-name" x="775" y="260">YOUR NAME</text>
    <rect class="name-rule" x="755" y="275" width="434" height="7"/>

    <text class="brand-name" font-size="76" x="972" y="528" text-anchor="middle">galavoyant</text>
  </g>

  <!-- Back of card -->
  <g class="card-back">
    <rect class="card-bg" x="220" y="775" width="1030" height="590" rx="40"/>
    <g clip-path="url(#backClip)">
      <polygon class="stripe-deep" points="267,775 375,775 498,1365 390,1365"/>
      <polygon class="stripe-mid" points="375,775 482,775 605,1365 498,1365"/>
      <polygon class="stripe-light" points="482,775 590,775 714,1365 605,1365"/>
    </g>
    <rect class="panel-outer" x="255" y="843" width="955" height="465" rx="30" filter="url(#panelShadow)"/>
    <rect class="panel-inner" x="285" y="857" width="898" height="438" rx="25" filter="url(#panelShadow)"/>
    <text class="brand-name" font-size="96" x="747" y="1128" text-anchor="middle">galavoyant</text>
  </g>
</svg>
</body>
</html>
```